Property investment company needs a letterhead design!

We are a new residential and commercial property investment company. Name of the company is Morvesta Group, LLC. We have a new logo and now we need letterhead! We prefer to have a professional and upscale appearance. We don't have any fixed requirements, so be creative! Thank you for considering this project. We are so excited to see what happens!

Target Market(s)

Professional

Industry/Entity Type

Real Estate Development

```html
<!DOCTYPE html>
<html lang="en">
<head>
<meta charset="utf-8">
<title>Morvesta Group, LLC — Letterhead</title>
<link rel="stylesheet" href="https://fonts.googleapis.com/css2?family=Open+Sans:wght@400;600;700&display=swap">
<style>
  :root {
    --navy: #0c2340;
    --sky: #29a8e0;
    --ink: #555a5f;
    --paper: #ffffff;
  }
  * { margin: 0; padding: 0; box-sizing: border-box; }
  html, body { width: 848px; height: 1200px; overflow: hidden; background: var(--paper); }
  body { font-family: "Open Sans", sans-serif; color: var(--ink); }
  .letterhead { position: relative; width: 848px; height: 1200px; }

  .brand { position: absolute; left: 96px; top: 86px; display: flex; align-items: center; gap: 12px; }
  .brand-dot { width: 42px; height: 42px; border-radius: 50%; background: var(--navy); }
  .brand-name { font-weight: 700; font-size: 34px; color: var(--navy); letter-spacing: 1px; }

  .company { position: absolute; left: 97px; top: 192px; }
  .company-name { font-weight: 700; font-size: 17px; letter-spacing: 0.2px; margin-bottom: 4px; }
  .company-line { font-size: 16.5px; line-height: 25.8px; display: flex; }
  .company-line .key { width: 30px; font-weight: 700; }
  .company-line .key.blue { color: var(--sky); }

  .salutation { position: absolute; left: 96px; top: 327px; font-weight: 700; font-size: 17px; }
  .date { position: absolute; right: 84px; top: 328px; font-size: 13px; }

  .body-text { position: absolute; left: 96px; top: 397px; width: 668px; font-size: 16.4px; line-height: 25.7px; text-align: justify; hyphens: manual; }
  .body-text p + p { margin-top: 25.7px; }

  .signature { position: absolute; left: 78px; top: 944px; width: 236px; height: 76px; background: linear-gradient(90deg, #f1f1f1, #e6e6e6); border-radius: 4px; }
  .signer { position: absolute; left: 97px; top: 1022px; }
  .signer-name { font-weight: 700; font-size: 17px; letter-spacing: -0.3px; }
  .signer-role { font-size: 16px; margin-top: 2px; letter-spacing: -0.3px; }

  .contacts { position: absolute; left: 475px; top: 1002px; list-style: none; }
  .contacts li { display: flex; align-items: center; height: 23px; margin-bottom: 12px; font-size: 16.8px; }
  .contacts li:nth-child(2) { margin-bottom: 9px; }
  .icon { width: 23px; height: 23px; background: var(--navy); margin-right: 14px; flex: none; }
  .icon svg { display: block; width: 23px; height: 23px; }

  .footer-band { position: absolute; left: 0; bottom: 0; width: 848px; height: 32px; background: var(--navy); }
</style>
</head>
<body>
<main class="letterhead">
  <div class="brand">
    <span class="brand-dot"></span>
    <span class="brand-name">MORVESTA</span>
  </div>

  <section class="company">
    <div class="company-name">MORVESTA GROUP,LLC</div>
    <div class="company-line"><span class="key blue">A :</span>27-4,Corliss Road Singapore - 4512</div>
    <div class="company-line"><span class="key">W:</span>www.MorvestaGroupLLC.com</div>
    <div class="company-line"><span class="key blue">P :</span>+880 - 55501 - 2468</div>
  </section>

  <div class="salutation">Dear, Rowan</div>
  <div class="date">Date, 10 September, 2020</div>

  <article class="body-text">
    <p>Contrary to popular belief, Lorem Ipsum is not simply random text. It has roots in a piece of classical Latin literature from 45 BC, making it over 2000 years old. Edwin Marlowe, a Latin professor at Ashbury Hill College in Virginia, looked up one of the more obscure Latin words, consectetur, from a Lorem Ipsum passage, and going through the cites of the word in classical literature, discovered the undoubt&shy;able source.</p>
    <p>Lorem Ipsum comes from sections 1.10.32 and 1.10.33 of "de Finibus Bonorum et Malorum" (The Extremes of Good and Evil) by Varenius, written in 45 BC. This book is a treatise on the theory of ethics, very popular during the Renaissance. Lorem Ipsum used since the 1500s is reproduced below for those interested. Sections 1.10.32 and 1.10.33 from "de Finibus Bonorum et Malorum" by Varenius are also reproduced in their exact original form, accompanied by English versions from the 1914 translation by H. Pembroke.</p>
    <p>Contrary to popular belief, Lorem Ipsum is not simply random text. It has roots in a piece of classical Latin literature from 45 BC, making it over 2000 years old. Edwin Marlowe, a Latin professor at Ashbury Hill College in Virginia, looked up one of the more obscure Latin words.</p>
  </article>

  <div class="signature" role="img" aria-label="Handwritten signature of Daniel R. Whitmore"></div>
  <div class="signer">
    <div class="signer-name">Daniel R. Whitmore</div>
    <div class="signer-role">General Director</div>
  </div>

  <ul class="contacts">
    <li><span class="icon"><svg viewBox="0 0 23 23"><path d="M11.5 4a5 5 0 0 0-5 5c0 3.6 5 9.5 5 9.5s5-5.9 5-9.5a5 5 0 0 0-5-5z" fill="#fff"/><circle cx="11.5" cy="9" r="2" fill="#0c2340"/></svg></span>18/B, Harbour Lane Street, Italy</li>
    <li><span class="icon"><svg viewBox="0 0 23 23"><path d="M6 5.5l3-.5 1.5 3.5-1.8 1.3a9 9 0 0 0 4.5 4.5l1.3-1.8 3.5 1.5-.5 3c-7 .5-12-4.5-11.5-11.5z" fill="#fff"/></svg></span>+880 100 200 3040</li>
    <li><span class="icon"><svg viewBox="0 0 23 23"><rect x="3.5" y="6.5" width="16" height="11" fill="none" stroke="#fff" stroke-width="1.3"/><path d="M3.5 6.5l8 6 8-6M3.5 17.5l6-5M19.5 17.5l-6-5" fill="none" stroke="#fff" stroke-width="1.1"/></svg></span>MorvestaGroupLLC@mvmail.com</li>
    <li><span class="icon"><svg viewBox="0 0 23 23"><g fill="none" stroke="#fff" stroke-width="1.2"><circle cx="11.5" cy="11.5" r="7"/><ellipse cx="11.5" cy="11.5" rx="3" ry="7"/><path d="M4.5 11.5h14M5.5 8h12M5.5 15h12"/></g></svg></span>www.MorvestaGroupLLC.com</li>
  </ul>

  <div class="footer-band"></div>
</main>
</body>
</html>
```